Organic Mavu (Coffee) Scrub Label for high end product

Need a product label for a coffee based body scrub called Mavu Body Scrub a 100% organic product. Our primary target is the yoga community so designs should reflect calm, perhaps incorporate eastern yoga symbology. simpler the better. Design should include both a round lid label and a rectangular wrap around label.

Target Market(s)

yoga community, people with cellulite, etc.

Industry/Entity Type

Community

```html
<!DOCTYPE html>
<html lang="en">
<head>
<meta charset="utf-8">
<title>Mavu Scrub – Lid and Wrap Labels</title>
<link rel="stylesheet" href="https://fonts.googleapis.com/css2?family=Montserrat:wght@600&family=Courier+Prime&display=swap">
<style>
  :root {
    --page: #ffffff;
    --lid-black: #0b0b0b;
    --wrap-charcoal: #262626;
    --gold: #b89a5f;
    --ivory: #e9e4da;
    --muted: #8d8a84;
  }
  * { margin: 0; padding: 0; box-sizing: border-box; }
  html, body { width: 1200px; height: 866px; overflow: hidden; background: var(--page); }
  .canvas { position: relative; width: 1200px; height: 866px; }

  .lid-label {
    position: absolute; left: 238px; top: 455px;
    width: 204px; height: 204px; border-radius: 50%;
    background: var(--lid-black);
    display: flex; flex-direction: column; align-items: center; justify-content: center;
  }
  .lid-label .ring {
    position: absolute; inset: 10px; border: 1.5px solid var(--gold); border-radius: 50%;
  }

  .wrap-label {
    position: absolute; left: 520px; top: 458px;
    width: 560px; height: 198px;
    background: var(--wrap-charcoal);
    display: grid; grid-template-columns: 160px 1fr 160px;
  }
  .wrap-label .rule {
    position: absolute; left: 0; right: 0; height: 1.5px; background: var(--gold);
  }
  .wrap-label .rule.top { top: 10px; }
  .wrap-label .rule.bottom { bottom: 10px; }

  .front-panel {
    display: flex; flex-direction: column; align-items: center; justify-content: center;
  }
  .side-panel {
    padding: 30px 18px; color: var(--muted);
    font-family: "Montserrat", sans-serif; font-weight: 600; font-size: 8px; line-height: 1.6;
  }
  .side-panel h3 { color: var(--ivory); font-size: 8px; font-weight: 600; margin-bottom: 4px; letter-spacing: 0.05em; }

  .brand-mark {
    width: 14px; height: 14px; border-radius: 50%; background: var(--gold); margin-bottom: 12px;
  }
  .brand-name {
    font-family: "Montserrat", sans-serif; font-weight: 600;
    color: var(--gold); font-size: 17px; letter-spacing: 0.01em;
  }
  .lid-label .brand-name { font-size: 15px; }
  .product-type {
    font-family: "Courier Prime", monospace; color: var(--ivory);
    font-size: 10px; margin-top: 18px;
  }
  .net-weight {
    font-family: "Montserrat", sans-serif; font-weight: 600; color: var(--ivory);
    font-size: 10px; margin-top: 18px;
  }
</style>
</head>
<body>
<main class="canvas">
  <section class="lid-label" aria-label="Round lid label">
    <span class="ring"></span>
    <span class="brand-mark"></span>
    <p class="brand-name">MAVU SCRUB</p>
    <p class="product-type">coffee body scrub</p>
  </section>

  <section class="wrap-label" aria-label="Wrap-around jar label">
    <span class="rule top"></span>
    <span class="rule bottom"></span>
    <div class="side-panel">
      <h3>DIRECTIONS</h3>
      <p>Apply to damp skin, massage gently, rinse well.</p>
    </div>
    <div class="front-panel">
      <span class="brand-mark"></span>
      <p class="brand-name">MAVU SCRUB</p>
      <p class="product-type">coffee body scrub</p>
      <p class="net-weight">16 OZ /454 G</p>
    </div>
    <div class="side-panel">
      <h3>INGREDIENTS</h3>
      <p>Organic coffee, coconut oil, brown sugar, sea salt.</p>
    </div>
  </section>
</main>
</body>
</html>
```